Medspa business needs a webpage

we need a website for a new Medspa company based in Lynden, WA called Tarn Meridian Medical Aesthetics. We offer non surgical, cosmetic procedures as well as medical weight loss. We would like a sleek design, with rich colors (dark, emerald green and gold). The website should list our services, pricing and links to book appointments.

```html
<!DOCTYPE html>
<html lang="en">
<head>
<meta charset="utf-8">
<title>Tarn Meridian Medical Aesthetics</title>
<link href="https://fonts.googleapis.com/css2?family=Montserrat:wght@200;300;400;500;600&display=swap" rel="stylesheet">
<style>
:root{
  --backdrop:#8a8a8a;
  --ink:#0e1b07;
  --forest:#2d3d23;
  --gold:#c1a044;
  --gold-soft:#d9c48a;
  --cream:#f7f3ea;
  --cream-warm:#fbf3dc;
  --text:#2a2a2a;
  --muted:#7b7466;
  --white:#ffffff;
}
*{box-sizing:border-box;margin:0;padding:0}
html,body{width:1200px;height:2724px;overflow:hidden}
body{background:var(--backdrop);font-family:'Montserrat',sans-serif;color:var(--text);position:relative}
.abs{position:absolute}
.page{position:absolute;left:81px;top:81px;width:1037px;height:2562px;background:var(--white);box-shadow:0 6px 22px rgba(0,0,0,.35)}

/* nav */
.nav{left:81px;top:81px;width:1037px;height:54px;background:var(--ink)}
.brand{left:290px;top:90px;color:var(--gold);font-weight:400;letter-spacing:4px;line-height:1.15}
.brand .n1{font-size:18px;display:block}
.brand .n2{font-size:10px;display:block;letter-spacing:3.4px}
.brand-dot{left:250px;top:90px;width:30px;height:30px;border:1px solid var(--gold)}
.menu{top:101px;font-size:10.5px;color:var(--white)}
.menu.active{color:var(--gold)}
.nav-book{left:989px;top:95px;width:71px;height:25px;border:1px solid var(--gold);color:var(--gold);font-size:10px;text-align:center;line-height:23px}

/* hero */
.hero{left:81px;top:135px;width:1037px;height:530px;background:radial-gradient(ellipse at 75% 35%,#fff9ea 0%,#fbefd0 55%,#f4e2b2 100%)}
.hero-art{left:230px;top:150px;width:310px;height:515px;background:linear-gradient(180deg,#efeae0 0%,#d9d2c3 55%,#c9b79a 100%);border-radius:150px 150px 0 0}
.hero-title{left:600px;top:236px;color:var(--gold);font-weight:200;font-size:64px;line-height:56px;letter-spacing:1px}
.hero-sub{left:602px;top:412px;color:var(--gold);font-weight:400;font-size:24px;letter-spacing:3px}
.hero-copy{left:602px;top:450px;width:300px;font-size:14px;line-height:19px;color:var(--muted)}
.btn{display:block;text-align:center;font-weight:400}
.btn-gold{background:var(--gold);color:var(--white)}
.btn-dark{background:var(--ink);color:var(--white)}
.hero-btn{top:506px;height:35px;line-height:35px;font-size:15px}

/* welcome */
.portrait{top:729px;width:166px;height:237px;background:linear-gradient(180deg,#8a8a86 0%,#5a544e 55%,#1f2119 100%)}
.portrait span{position:absolute;bottom:12px;left:0;width:100%;text-align:center;color:var(--white);font-size:13.5px}
.welcome-kicker{left:625px;top:747px;font-size:16px;color:var(--ink)}
.welcome-name{left:623px;top:768px;color:var(--gold);font-weight:300;font-size:45px;line-height:46px}
.welcome-name2{left:624px;top:810px;color:var(--gold);font-weight:300;font-size:30px}
.welcome-copy{left:627px;top:845px;width:320px;font-size:9.6px;line-height:14px;color:var(--muted)}
.welcome-btn{left:625px;top:927px;width:86px;height:24px;line-height:24px;font-size:9.5px}

/* services */
.services{left:81px;top:1023px;width:1037px;height:377px;background:var(--cream)}
.section-title{left:81px;width:1037px;text-align:center;color:var(--gold);font-weight:200;font-size:46px;letter-spacing:1px}
.svc{top:1137px;width:219px;height:196px;border:1px solid var(--gold-soft);padding:22px 8px 22px 22px}
.svc-dark{background:linear-gradient(90deg,#2a3a22 0%,#3b4a30 50%,#2a3a22 100%);border-color:var(--gold)}
.svc-icon{width:26px;height:26px}
.svc h3{font-weight:400;font-size:16.5px;color:var(--ink);margin-top:10px;white-space:nowrap}
.svc-dark h3{color:var(--white)}
.svc ul{list-style:none;margin-top:6px;font-size:10.5px;line-height:18.5px;color:var(--muted)}
.svc-dark ul{color:var(--white)}
.svc li:before{content:"– ";color:var(--gold)}
.svc-btn{position:absolute;left:22px;top:150px;height:24px;line-height:24px;padding:0 9px;font-size:10px}

/* pricing */
.price{top:1527px;width:207px;height:203px;border:1px solid var(--gold-soft);padding:20px 6px 20px 21px}
.price h3{font-weight:400;font-size:16px;color:var(--ink);white-space:nowrap}
.price .amt{margin-top:12px;color:var(--gold);font-weight:300;font-size:21px;white-space:nowrap}
.price .amt small{font-size:11px}
.price ul{list-style:none;margin-top:10px;font-size:9.5px;line-height:18.5px;color:var(--muted);white-space:nowrap}
.price li:before{content:"– ";color:var(--gold)}
.price-btn{position:absolute;left:21px;top:159px;width:53px;height:24px;line-height:24px;font-size:9.5px}
.price-note{left:81px;top:1753px;width:1037px;text-align:center;font-size:9.5px;color:var(--muted)}

/* call to action */
.cta-photo{left:81px;top:1827px;width:733px;height:356px;background:linear-gradient(90deg,#dfe0e6 0%,#e8c9b4 35%,#e2bca4 60%,#c9c8e6 85%,#eef0f4 100%)}
.cta-box{left:600px;top:1943px;width:436px;height:271px;background:var(--cream)}
.cta-frame{left:611px;top:1953px;width:414px;height:251px;border:1px solid var(--gold-soft)}
.cta-title{left:600px;top:1997px;width:436px;text-align:center;font-weight:300;font-size:46px;color:var(--ink)}
.cta-copy{left:600px;top:2058px;width:436px;text-align:center;font-size:16.5px;line-height:24px;color:var(--ink)}
.cta-btn{top:2125px;height:30px;line-height:30px;font-size:13.5px}

/* contact */
.form{left:250px;top:2240px;width:309px;height:324px;border:1px solid #eeeeee;padding:19px 12px}
.form label{display:block;font-size:10px;color:var(--ink);margin-bottom:7px}
.field{height:25px;border:1px solid #cfcfcf;font-size:7.5px;color:#777;padding:0 9px;line-height:24px;margin-bottom:11px;position:relative}
.field.area{height:56px;font-family:monospace;font-size:8px}
.send{height:24px;line-height:24px;text-align:center;font-size:8px;font-weight:600;color:var(--white);background:var(--gold);margin-top:6px}
.form-note{font-size:8px;color:var(--ink);margin-top:12px}
.visit-title{left:600px;top:2280px;font-weight:300;font-size:46px;color:var(--gold)}
.visit-addr{left:600px;top:2339px;font-size:10px;color:var(--muted)}
.visit-dir{left:600px;top:2358px;font-weight:300;font-size:22px;color:var(--gold)}
.visit-list{left:600px;top:2391px;list-style:none;font-size:10px;line-height:18.5px;color:var(--muted)}
.visit-list li:before{content:"– ";color:var(--gold)}

/* footer */
.footer{left:81px;top:2598px;width:1037px;height:45px;background:var(--ink)}
.foot-copy{left:248px;top:2615px;font-size:9.5px;color:var(--white)}
.foot-links{left:751px;top:2616px;font-size:9.5px;color:var(--white);word-spacing:2px}
</style>
</head>
<body>
<div class="page"></div>

<header>
  <div class="abs nav"></div>
  <div class="abs brand-dot" aria-hidden="true"></div>
  <div class="abs brand"><span class="n1">TARN MERIDIAN</span><span class="n2">MEDICAL AESTHETICS</span></div>
  <span class="abs menu active" style="left:704px">Home</span>
  <span class="abs menu" style="left:758px">Services</span>
  <span class="abs menu" style="left:823px">Pricing</span>
  <span class="abs menu" style="left:880px">Team</span>
  <span class="abs menu" style="left:929px">Contact</span>
  <span class="abs nav-book">Book Now</span>
</header>

<section>
  <div class="abs hero"></div>
  <div class="abs hero-art" role="img" aria-label="Classical marble statue of a woman in a flowing gown"></div>
  <h1 class="abs hero-title">ELEVATE<br>YOUR SKIN.<br>ENHANCE</h1>
  <div class="abs hero-sub">YOUR CONFIDENCE.</div>
  <p class="abs hero-copy">Non-surgical aesthetic treatments and medical weight loss in Lynden, WA.</p>
  <a class="abs btn btn-gold hero-btn" style="left:602px;width:186px">Book an Appointment</a>
  <a class="abs btn btn-dark hero-btn" style="left:797px;width:152px">Explore Services</a>
</section>

<section>
  <div class="abs portrait" style="left:248px" role="img" aria-label="Portrait of nurse practitioner Maren Holt"><span>Maren Holt | ARNP</span></div>
  <div class="abs portrait" style="left:422px" role="img" aria-label="Portrait of physician assistant Leila Ortega"><span>Leila Ortega | PA-C</span></div>
  <div class="abs welcome-kicker">WELCOME TO</div>
  <h2 class="abs welcome-name">TARN MERIDIAN</h2>
  <div class="abs welcome-name2">MEDICAL AESTHETICS</div>
  <p class="abs welcome-copy">Lorem ipsum dolor sit amet, consectetuer adipiscing elit, sed diam nonummy nibh euismod tincidunt ut laoreet dolore magna aliquam erat volutpat. Ut wisi enim ad minim veniam, quis nostrud exerci tation ullamcorper suscipit lobortis nisl ut aliquip ex ea commodo consequat.</p>
  <a class="abs btn btn-dark welcome-btn">LEARN MORE</a>
</section>

<section>
  <div class="abs services"></div>
  <h2 class="abs section-title" style="top:1060px">OUR SERVICES</h2>

  <div class="abs svc" style="left:248px">
    <svg class="svc-icon" viewBox="0 0 26 26" fill="none" stroke="#c1a044" stroke-width="1.2"><circle cx="12" cy="9" r="6"/><path d="M3 25c1-6 5-9 9-9s8 3 9 9"/></svg>
    <h3>INJECTABLES</h3>
    <ul><li>Wrinkle Relaxers</li><li>Lip &amp; Cheek Filler</li><li>Jawline &amp; Chin Contour</li></ul>
    <a class="btn btn-gold svc-btn">Book injectables →</a>
  </div>

  <div class="abs svc svc-dark" style="left:491px" role="img" aria-label="Dimmed close-up of a woman's glowing skin behind the card">
    <svg class="svc-icon" viewBox="0 0 26 26" fill="none" stroke="#ffffff" stroke-width="1.2"><circle cx="13" cy="13" r="10"/><path d="M13 3v20M3 13h20"/></svg>
    <h3>Skin Rejuvenation</h3>
    <ul><li>Microneedling</li><li>Medical-grade Peels</li><li>LED &amp; Collagen Therapy</li></ul>
    <a class="btn btn-gold svc-btn">Book skin rejuvenation →</a>
  </div>

  <div class="abs svc" style="left:734px">
    <svg class="svc-icon" viewBox="0 0 26 26" fill="none" stroke="#c1a044" stroke-width="1.2"><path d="M6 3v6M20 3v6M5 9h16l-2 15H7z"/></svg>
    <h3>Medical Weight Loss</h3>
    <ul><li>Consultation &amp; Labs</li><li>GLP-1 Assisted Plans</li><li>Nutrition &amp; Coaching</li></ul>
    <a class="btn btn-gold svc-btn">Book weight loss consult →</a>
  </div>
</section>

<section>
  <h2 class="abs section-title" style="top:1446px">TRANSPARENT PRICING</h2>

  <div class="abs price" style="left:163px">
    <h3>Neuromodulators</h3>
    <div class="amt">$12–$14 <small>/ unit</small></div>
    <ul><li>Forehead, Glabella, Crow's Feet</li><li>Treatment plan review</li><li>Follow-up tweak within 2 weeks</li></ul>
    <a class="btn btn-gold price-btn">Book →</a>
  </div>
  <div class="abs price" style="left:385px">
    <h3>Dermal Fillers</h3>
    <div class="amt">$650–$800 <small>/ syringe</small></div>
    <ul><li>Forehead, Glabella, Crow's Feet</li><li>Treatment plan review</li><li>Follow-up tweak within 2 weeks</li></ul>
    <a class="btn btn-gold price-btn">Book →</a>
  </div>
  <div class="abs price" style="left:607px">
    <h3>Microneedling</h3>
    <div class="amt">$299 <small>/ session</small></div>
    <ul><li>Forehead, Glabella, Crow's Feet</li><li>Treatment plan review</li><li>Follow-up tweak within 2 weeks</li></ul>
    <a class="btn btn-gold price-btn">Book →</a>
  </div>
  <div class="abs price" style="left:829px">
    <h3>Weight Loss Program</h3>
    <div class="amt">$249 <small>/ month</small></div>
    <ul><li>Forehead, Glabella, Crow's Feet</li><li>Treatment plan review</li><li>Follow-up tweak within 2 weeks</li></ul>
    <a class="btn btn-gold price-btn">Book →</a>
  </div>
  <p class="abs price-note">* Pricing shown for contest demo. Final quotes provided after consultation.</p>
</section>

<section>
  <div class="abs cta-photo" role="img" aria-label="Woman's face held by gloved hands during an aesthetic treatment"></div>
  <div class="abs cta-box"></div>
  <div class="abs cta-frame"></div>
  <h2 class="abs cta-title">Ready to glow?</h2>
  <p class="abs cta-copy">Reserve your appointment in minutes.<br>New patients welcome.</p>
  <a class="abs btn btn-gold cta-btn" style="left:695px;width:100px">Book Online</a>
  <a class="abs btn btn-dark cta-btn" style="left:804px;width:136px">Call (360) 555-0178</a>
</section>

<section>
  <form class="abs form">
    <label>Name</label><div class="field">Your full name</div>
    <label>Email</label><div class="field">you@example.com</div>
    <label>Service</label><div class="field" style="color:#222">Injectables<svg style="position:absolute;right:5px;top:9px" width="7" height="5" viewBox="0 0 7 5"><path d="M0 0l3.5 4L7 0" fill="none" stroke="#333"/></svg></div>
    <label>Message</label><div class="field area">Tell us your goals</div>
    <div class="send">Send Message</div>
    <p class="form-note">Demo form for contest—replace with platform form or CRM embed.</p>
  </form>
  <h2 class="abs visit-title">Visit Us</h2>
  <p class="abs visit-addr">48 Cedar Row, Lynden, WA 98264</p>
  <div class="abs visit-dir">Get directions →</div>
  <ul class="abs visit-list"><li>Call: (360) 555-0178</li><li>Email: hello@tarnmeridian.com</li><li>Book online</li></ul>
</section>

<footer>
  <div class="abs footer"></div>
  <p class="abs foot-copy">© 2025 Tarn Meridian Medical Aesthetics · Lynden, WA</p>
  <p class="abs foot-links">Services &nbsp;| &nbsp;Pricing &nbsp;| &nbsp;Book &nbsp;| &nbsp;Privacy</p>
</footer>
</body>
</html>
```